K & M Wheel Depot business cards

need business card for tire/car care company based in tampa, florida. we sell used and new tires, also we service vehicles, tune ups, oil chasnge, brakes and A/c we offer free towing with major vehicle repair and tire purchase. we also offer free estimates on any engine or a/c repair. also we have the lowest price in the city on used and new tires.

Contact Information for Business Card

4170 E Marigold Blvd,
Tampa, Fl 33581
Ph: 813-572-3186
KandMWheelDepot@Mailverse.com

Font styles to use
Serif
Sans Serif
Decorative

Requirements
Must have
• my logo, what we do ( used and new tires , oil change, brakes, tune ups, free towing vehicl. Also business info.
Nice to have
• an image of a towing truck, highlighting that we offer free towing. something close to what i have in one of the attached image

```html
<!DOCTYPE html>
<html lang="en">
<head>
<meta charset="utf-8">
<title>K &amp; M Wheel Depot — Business Cards</title>
<link rel="stylesheet" href="https://fonts.googleapis.com/css2?family=Tinos:wght@400;700&display=swap">
<style>
  :root {
    --stage: #e4e6e8;
    --card-white: #ffffff;
    --card-grey: #eceeef;
    --brand-blue: #0b95c8;
    --band-top: #0a7fb8;
    --band-bottom: #119fd0;
    --ink-dark: #1d1f22;
    --shadow: rgba(0, 0, 0, 0.18);
  }
  * { margin: 0; padding: 0; box-sizing: border-box; }
  html, body {
    width: 1200px; height: 922px; overflow: hidden;
    background: var(--stage);
    font-family: "Tinos", "Times New Roman", serif;
  }
  .canvas { position: relative; width: 1200px; height: 922px; }

  .card {
    position: absolute;
    width: 640px; height: 366px;
    border-radius: 22px;
    overflow: hidden;
    box-shadow: 0 10px 30px var(--shadow);
  }

  /* Front */
  .card-front {
    left: 60px; top: 70px;
    background: linear-gradient(160deg, var(--card-white) 0%, var(--card-grey) 100%);
    display: flex; align-items: center; justify-content: center;
  }
  .brand {
    display: flex; align-items: center; gap: 18px;
  }
  .brand-dot {
    width: 54px; height: 54px; border-radius: 50%;
    background: var(--ink-dark);
  }
  .brand-name {
    font-weight: 700; font-size: 46px; color: var(--ink-dark);
    white-space: nowrap;
  }

  /* Back */
  .card-back {
    left: 500px; top: 490px;
    background: var(--card-white);
  }
  .card-back .brand {
    position: absolute; left: 34px; top: 92px; gap: 12px;
  }
  .card-back .brand-dot { width: 38px; height: 38px; }
  .card-back .brand-name { font-size: 30px; }

  .contact {
    position: absolute; right: 30px; top: 36px;
    width: 300px; text-align: center;
    color: var(--brand-blue);
  }
  .employee-name { font-weight: 700; font-size: 38px; line-height: 1; }
  .employee-role { font-size: 19px; margin-top: 2px; }
  .phone { font-size: 24px; margin-top: 62px; }
  .email { font-size: 21px; margin-top: 6px; white-space: nowrap; }

  .address-band {
    position: absolute; left: 0; right: 0; bottom: 0; height: 92px;
    background: linear-gradient(180deg, var(--band-top), var(--band-bottom));
    color: var(--card-white);
    font-size: 25px;
    display: flex; align-items: center; padding-left: 56px;
  }
</style>
</head>
<body>
<main class="canvas">
  <section class="card card-front" aria-label="Business card front">
    <div class="brand">
      <span class="brand-dot"></span>
      <span class="brand-name">K &amp; M Wheel Depot</span>
    </div>
  </section>

  <section class="card card-back" aria-label="Business card back">
    <div class="brand">
      <span class="brand-dot"></span>
      <span class="brand-name">K &amp; M Wheel Depot</span>
    </div>
    <div class="contact">
      <p class="employee-name">Employee name</p>
      <p class="employee-role">Managing Director</p>
      <p class="phone">813-572-3186</p>
      <p class="email">KandMWheelDepot@Mailverse.com</p>
    </div>
    <div class="address-band">4170 E Marigold Blvd, Tampa, Fl 33581</div>
  </section>
</main>
</body>
</html>
```